Business Card for Multi-Brand Sportswear Company

We are looking for a business card which represents our company and the multiple brands within it.

The company: Kelt Athletic (LTD)
The brands: Kelt, PawaLuni, VerdantFlex, Grit and Gale

Employees using these cards would be representing Kelt Athletic, rather than any of the individual brands. You will see a current design within the uploaded files, to give some inspiration. The actual text of the brands is not necessary, but the logos should be on there is some format.

Our creative minds on this are stretched, so we are looking for someone to make this their own, and show us what a good business card should look like.

We may like to get these printed with spot gloss, so keep that in mind with your designs.

www.keltathletic.co.uk

Industry/Entity Type

Business

Contact Information for Business Card

Tom Hollingsworth-Pryce
Operations Manager
(+44) 1632 960 418
Tom@keltathletic.co.uk
www.keltathletic.co.uk

Font styles to use
Sans Serif
Other font styles liked:
• Eurostile

Colors
ffffff

Requirements
Nice to have
• Dark (black) background

```html
<!DOCTYPE html>
<html lang="en">
<head>
<meta charset="utf-8">
<title>Kelt Athletic – Business Card</title>
<link rel="stylesheet" href="https://fonts.googleapis.com/css2?family=Exo+2:wght@400;700&display=swap">
<style>
  :root {
    --backdrop: #3b2a30;
    --card-black: #000000;
    --brand-red: #ec1f27;
    --ink-white: #ffffff;
    --muted-grey: #8a8590;
    --type: "Exo 2", sans-serif;
  }
  * { margin: 0; padding: 0; box-sizing: border-box; }
  html, body {
    width: 1200px; height: 1200px; overflow: hidden;
    background: var(--backdrop);
    font-family: var(--type);
  }
  .card {
    position: absolute;
    left: 262px;
    width: 676px; height: 384px;
    background: var(--card-black);
    border-radius: 20px;
    overflow: hidden;
  }
  .card--front { top: 197px; }
  .card--back  { top: 620px; }

  .front-wordmark {
    position: absolute; left: 0; right: 0; top: 158px;
    text-align: center;
    color: var(--ink-white);
    font-size: 54px; font-weight: 400; letter-spacing: 2px;
  }

  .back-graphics { position: absolute; inset: 0; }

  .holder { position: absolute; left: 33px; top: 78px; color: var(--ink-white); }
  .holder-name { font-size: 30px; line-height: 34px; }
  .holder-name .first { font-weight: 700; }
  .holder-name .last { font-weight: 400; }
  .holder-role { font-size: 19px; line-height: 26px; margin-top: 2px; }

  .band-wordmark {
    position: absolute; right: 30px; top: 116px;
    color: var(--card-black);
    font-size: 30px; font-weight: 400; letter-spacing: 1px;
  }

  .contact-list { position: absolute; right: 0; top: 189px; list-style: none; }
  .contact-row {
    display: flex; align-items: center; justify-content: flex-end;
    height: 32px; margin-bottom: 5px;
  }
  .contact-text { color: var(--ink-white); font-size: 19px; margin-right: 6px; }
  .contact-tab {
    width: 56px; height: 32px;
    background: var(--brand-red);
    border-radius: 16px 0 0 16px;
    display: flex; align-items: center; padding-left: 12px;
  }
  .contact-tab svg { width: 20px; height: 20px; }

  .address {
    position: absolute; left: 33px; top: 328px;
    color: var(--ink-white); font-size: 14px; line-height: 18px;
  }
  .brand-row { list-style: none; }
  .brand-name {
    position: absolute; top: 328px;
    width: 90px; margin-left: -45px;
    text-align: center;
    font-size: 12px; line-height: 18px; font-weight: 400;
    white-space: nowrap;
  }
  .brand-name--pawaluni { left: 370px; color: var(--muted-grey); }
  .brand-name--grit     { left: 450px; color: var(--brand-red); }
  .brand-name--kelt     { left: 538px; color: var(--ink-white); }
  .brand-name--verdant  { left: 622px; color: var(--muted-grey); }
</style>
</head>
<body>

<section class="card card--front">
  <div class="front-wordmark">KELT ATHLETIC</div>
</section>

<section class="card card--back">
  <svg class="back-graphics" width="676" height="384" viewBox="0 0 676 384">
    <polygon class="red-band" fill="var(--brand-red)"
      points="0,156 250,156 328,86 676,86 676,174 328,174 259,244 0,244"/>
    <g fill="var(--card-black)">
      <polygon points="10,244 20,244 108,156 98,156"/>
      <polygon points="86,244 96,244 184,156 174,156"/>
      <polygon points="166,244 176,244 264,156 254,156"/>
    </g>
  </svg>

  <div class="holder">
    <p class="holder-name"><span class="first">Rhys</span> <span class="last">Penhallow</span></p>
    <p class="holder-role">Managing Director</p>
  </div>

  <div class="band-wordmark">KELT ATHLETIC</div>

  <ul class="contact-list">
    <li class="contact-row">
      <span class="contact-text">+44 (0) 1632 960418</span>
      <span class="contact-tab">
        <svg viewBox="0 0 20 20"><path fill="#000" d="M5 2h3l1.5 4-2 1.3a9 9 0 0 0 5.2 5.2l1.3-2 4 1.5v3a2 2 0 0 1-2 2A15 15 0 0 1 3 4a2 2 0 0 1 2-2z"/></svg>
      </span>
    </li>
    <li class="contact-row">
      <span class="contact-text">rhys@keltathletic.co.uk</span>
      <span class="contact-tab">
        <svg viewBox="0 0 20 20"><rect x="2" y="4.5" width="16" height="11" fill="none" stroke="#000" stroke-width="1.8"/><path d="M2 4.5l8 6.5 8-6.5" fill="none" stroke="#000" stroke-width="1.8"/></svg>
      </span>
    </li>
    <li class="contact-row">
      <span class="contact-text">www.keltathletic.co.uk</span>
      <span class="contact-tab">
        <svg viewBox="0 0 20 20" fill="none" stroke="#000" stroke-width="1.5"><circle cx="10" cy="10" r="8"/><ellipse cx="10" cy="10" rx="3.5" ry="8"/><path d="M2 10h16M3.5 6h13M3.5 14h13"/></svg>
      </span>
    </li>
  </ul>

  <p class="address">East Park, Harlow, Ripley, HG9 4XT</p>

  <ul class="brand-row">
    <li class="brand-name brand-name--pawaluni">PawaLuni</li>
    <li class="brand-name brand-name--grit">Grit and Gale</li>
    <li class="brand-name brand-name--kelt">Kelt</li>
    <li class="brand-name brand-name--verdant">VerdantFlex</li>
  </ul>
</section>

</body>
</html>
```